Bluestone Advisory & Mgmt - Professional Business Cards

Hi!

I am a Real Estate Developer and Construction Consultant.

I have a lot of inspiration from previous designs and would be open to using the attached Designs as a starting point. I would like to see these styles incorporated into your designs.

I really need professional business card to go with it that includes my important info.

Look forward to seeing your designs!.

Target Market(s)

My Target market are building owners, lawyers, consultants.

Industry/Entity Type

Real Estate Development

Contact Information for Business Card

My Name: Daniel Korvash
My Title: Principle
Company Name: Bluestone Advisory & Mgmt, LLC
Address: 348 West 41st Street, 7th FL New York, NY 10036
Mobile: 917.608.3719
Website: bam-hqx.com

Font styles to use
Serif
Sans Serif

Colors

Designer to choose colors to be used in the design.

Requirements
Must have
• Must incorporate the logo attached or have new that looks similar.
• Must use professional font that will be seen and judged by wealthy land owners and developers.
• Must incorporate some of the color green.
Should not have
• Photo's or pictures of people or buildings of any kind.

```html
<!DOCTYPE html>
<html lang="en">
<head>
<meta charset="utf-8">
<title>Bluestone Advisory &amp; Mgmt – Business Card</title>
<link rel="stylesheet" href="https://fonts.googleapis.com/css2?family=Raleway:wght@500&family=Roboto:wght@300;400;500&display=swap">
<style>
  :root {
    --backdrop: #cbcbcb;
    --card-white: #ffffff;
    --card-taupe: #9b9392;
    --brand-green: #4bb677;
    --text-grey: #9a9392;
    --text-white: #ffffff;
  }
  * { box-sizing: border-box; margin: 0; padding: 0; }
  html, body {
    width: 1125px; height: 1200px; overflow: hidden;
    background: var(--backdrop);
  }
  .canvas { position: relative; width: 1125px; height: 1200px; }
  .card {
    position: absolute; left: 150px; width: 825px; height: 470px;
    border-radius: 22px;
  }
  .card--front { top: 98px; background: var(--card-white); }
  .card--back { top: 632px; background: var(--card-taupe); }

  .wordmark {
    position: absolute;
    font-family: "Raleway", sans-serif; font-weight: 500;
    line-height: 1.1;
  }
  .card--front .wordmark {
    left: 118px; top: 168px; font-size: 34px; color: var(--brand-green);
  }
  .card--back .wordmark {
    left: 0; right: 0; top: 150px; text-align: center;
    font-size: 56px; color: var(--text-white);
  }

  .contact { position: absolute; left: 452px; top: 158px; font-family: "Roboto", sans-serif; }
  .contact__name { font-size: 29px; font-weight: 500; color: var(--brand-green); line-height: 1.2; }
  .contact__title { font-size: 18px; font-weight: 400; color: var(--text-grey); margin-top: 2px; }
  .contact__list { list-style: none; margin-top: 40px; }
  .contact__item {
    display: flex; align-items: center; gap: 7px;
    font-size: 21px; font-weight: 400; color: var(--text-grey); line-height: 28px;
  }
  .contact__item svg { flex: none; }
  .contact__web-host { color: var(--brand-green); }

  .address {
    position: absolute; left: 0; right: 0; top: 408px; text-align: center;
    font-family: "Roboto", sans-serif; font-weight: 400; font-size: 21px; color: var(--text-grey);
  }
</style>
</head>
<body>
<main class="canvas">
  <section class="card card--front">
    <div class="wordmark">Bluestone<br>Advisory &amp; Mgmt</div>
    <div class="contact">
      <h1 class="contact__name">Daniel Korvash</h1>
      <p class="contact__title">Principle</p>
      <ul class="contact__list">
        <li class="contact__item">
          <svg width="14" height="22" viewBox="0 0 14 22" aria-hidden="true">
            <rect x="1.5" y="1.5" width="11" height="19" rx="2" fill="none" stroke="#4bb677" stroke-width="2"/>
            <line x1="5" y1="17" x2="9" y2="17" stroke="#4bb677" stroke-width="1.6"/>
          </svg>
          917.608.3719
        </li>
        <li class="contact__item">
          <svg width="18" height="18" viewBox="0 0 18 18" aria-hidden="true">
            <circle cx="9" cy="9" r="8.5" fill="#4bb677"/>
            <circle cx="9" cy="9" r="3" fill="#fff"/>
          </svg>
          <span>www.<span class="contact__web-host">bam-hqx</span>.com</span>
        </li>
      </ul>
    </div>
    <p class="address">348 West 41st Street, 7th FL New York, NY 10036</p>
  </section>

  <section class="card card--back">
    <div class="wordmark">Bluestone<br>Advisory &amp; Mgmt</div>
  </section>
</main>
</body>
</html>
```